依頼詳細
ウコンのパッケージデザイン(ボトルシール)を依頼させて頂きます。「健康」「お酒にはウコン!!」というイメージをパッケージから感じることができ、ターゲットである居酒屋のお客さんが、何気に注文したくなるデザインを希望します。

・「健康ウコンふりかけ」の“健康”は小さめな字(メインはウコンふりかけ)

・食品表示ありのバージョンもお願いします。
「名称」ウコンふりかけ 「原材料名」秋ウコン(沖縄県産) 「内容量」12g 「賞味期限」 「保存方法」直射日光、高温多湿を避けて保存してください。 「販売者」K&M、沖縄県名護市字北原台4、TEL(FAX)0980-47-2935 その他リサイクル表示やバーコードなど必要なものがあればお願いします。

・希望として色の数はなるべく抑えたいたいです。(経費削減のため)
記載項目
ガラス容器
サイズ:W37mm×H87mm(写真は添付資料参照)
印刷:カラー印刷
紙質:ユポ紙or透明PET
希望イメージ
シンプル 複雑
単色 カラフル
暗い 明るい
日常 高級
遊び心 厳粛
未来的 伝統的
女性的 男性的
希望する色
黄色やゴールド(元気、健康的なイメージ)
納品ファイル
• 高解像度JPG (.jpg)
• イラストレーター形式 (.ai)
• PNG形式 (.png)
補足説明
・添付資料(写真)の容器のキャップは赤になってますが、使用する物は緑となります。

・独立し最初の商品作りでこういった依頼も初めてなので、皆様の多くの依頼をお待ちしております。是非よろしくお願い致します。
「MADE IN OKINAWA」の文字の記載(小さめ)もよろしくお願いします。
・容器の大きさのイメージとしてはよくある唐辛子調味料と同じような大きさです。
すでにすばらしいご提案を頂いておりますが、もう少し多くのご提案を見てみたい為、一週間延長させて頂きます。選定確約もさせて頂きますので、たくさんのご応募をお待ちしております。よろしくお願いします。

一番イメージに近いデザインだったというのが、一番の選択理由です。

はじめての依頼でしたが、提案して頂いた皆様の作品すべてが参考になりました。本当にありがとうございます。

```html
<!DOCTYPE html>
<html lang="ja">
<head>
<meta charset="utf-8">
<title>ウコンふりかけ ボトルラベル</title>
<link href="https://fonts.googleapis.com/css2?family=Dela+Gothic+One&family=Noto+Sans+JP:wght@400;700;900&display=swap" rel="stylesheet">
<style>
  :root{
    --bg:#ecebe6;
    --label:#111010;
    --gold:#f7c21b;
    --gold-deep:#e38a0c;
    --orange:#ea6a0f;
    --red:#c9161d;
    --white:#ffffff;
    --ink:#1a1a1a;
    --root-light:#e2b877;
    --root-dark:#9c6a2e;
  }
  *{box-sizing:border-box;margin:0;padding:0}
  html,body{width:800px;height:1200px;overflow:hidden;background:var(--bg)}
  body{font-family:"Noto Sans JP",sans-serif;position:relative}
  .label{position:absolute;left:20px;top:470px;width:760px;height:250px;background:var(--label);border-radius:4px;overflow:hidden}
  .badge{position:absolute;left:24px;top:14px;width:118px;height:118px}
  .badge-text{position:absolute;inset:0;display:flex;flex-direction:column;align-items:center;justify-content:center;color:var(--red);font-weight:900;line-height:1.1;transform:rotate(-10deg)}
  .badge-text .small{font-size:17px}
  .badge-text .big{font-size:23px}
  .root-photo{position:absolute;left:14px;top:128px;width:170px;height:112px;border-radius:40% 50% 30% 45%;background:radial-gradient(ellipse at 45% 40%,var(--root-light),var(--root-dark) 80%,transparent 82%)}
  .title-block{position:absolute;left:186px;top:12px;width:272px;height:226px}
  .hangover{position:absolute;left:22px;top:2px;padding:2px 10px;border:1.5px solid var(--gold);color:var(--gold);font-weight:700;font-size:15px;letter-spacing:1px;white-space:nowrap}
  .health{position:absolute;left:0;top:48px;width:30px;background:var(--orange);color:var(--white);font-weight:900;font-size:22px;line-height:1.05;text-align:center;padding:4px 0;border-radius:3px}
  .title-main{position:absolute;left:36px;top:32px;font-family:"Dela Gothic One",sans-serif;font-size:72px;line-height:1;white-space:nowrap;background:linear-gradient(180deg,var(--gold) 30%,var(--gold-deep));-webkit-background-clip:text;background-clip:text;color:transparent}
  .title-sub{position:absolute;left:56px;top:120px;font-family:"Dela Gothic One",sans-serif;font-size:42px;line-height:1;white-space:nowrap;color:var(--gold)}
  .curcumin{position:absolute;left:10px;top:194px;color:var(--gold);font-size:12px;font-weight:700;letter-spacing:.5px;white-space:nowrap}
  .info{position:absolute;left:470px;top:12px;width:276px;height:226px;background:var(--white);color:var(--ink);padding:8px 10px;font-size:11px;line-height:1.45}
  .facts{width:100%;border-collapse:collapse;margin-bottom:8px}
  .facts th,.facts td{border:1px solid var(--ink);padding:1px 5px;text-align:left;font-weight:400}
  .facts th{width:70px;white-space:nowrap}
  .facts td.blank{height:18px}
  .storage{margin-bottom:4px}
  .seller{margin-bottom:6px}
  .footer{display:flex;align-items:center;justify-content:space-between}
  .recycle{display:flex;gap:6px;align-items:center;font-size:9px}
  .mark{display:inline-flex;align-items:center;justify-content:center;width:24px;height:20px;border:1px solid var(--ink);border-radius:4px;font-size:10px;font-weight:700}
  .made{font-size:10px;font-weight:700;letter-spacing:.5px}
</style>
</head>
<body>
  <div class="label">
    <div class="badge">
      <svg width="118" height="118" viewBox="0 0 118 118" aria-hidden="true">
        <polygon fill="var(--gold)" points="59,2 69,20 88,9 89,30 110,29 100,48 117,59 100,70 110,89 89,88 88,109 69,98 59,116 49,98 30,109 29,88 8,89 18,70 1,59 18,48 8,29 29,30 30,9 49,20"/>
      </svg>
      <div class="badge-text"><span class="small">お酒には</span><span class="big">ウコン!!</span></div>
    </div>
    <div class="root-photo" role="img" aria-label="秋ウコンの根茎の写真"></div>

    <div class="title-block">
      <div class="hangover">二日酔いの予防・緩和</div>
      <div class="health">健<br>康</div>
      <div class="title-main">ウコン</div>
      <div class="title-sub">ふりかけ</div>
      <div class="curcumin">肝機能を強化するクルクミン入り</div>
    </div>

    <div class="info">
      <table class="facts">
        <tr><th>名称</th><td>ウコンふりかけ</td></tr>
        <tr><th>原材料名</th><td>秋ウコン(沖縄県産)</td></tr>
        <tr><th>内容量</th><td>12g</td></tr>
        <tr><th>賞味期限</th><td class="blank"></td></tr>
      </table>
      <p class="storage">保存方法：直射日光、高温多湿を避けて保存してください。</p>
      <p class="seller">販売者：K&amp;M<br>沖縄県名護市字北原台4<br>TEL(FAX)0980-47-2935</p>
      <div class="footer">
        <div class="recycle">
          <span class="mark">プラ</span><span>キャップ</span>
          <span class="mark">紙</span><span>ラベル</span>
        </div>
        <span class="made">MADE IN OKINAWA</span>
      </div>
    </div>
  </div>
</body>
</html>
```